Flyer-Design für Ferienhaus auf Sylt
Sehr professionelle und erfolgreiche Zusammenarbeit! Es hat alles reibungslos funktioniert und es wurde auf alle Wünsche eingegangen. Auch die Bildbearbeitung wurde umgehend umgesetzt. Der Designer hat alles verständlich erklärt und ich würde ihn jederzeit wieder beauftragen. Vielen Dank!
Zielgruppe
Ferienhaus auf Sylt im ruhigen und traditionellen Ort Archsum. Zielgruppe ruhe- und erholungssuchende Erwachsene, Familien mit Kind und evtl. mit Hund. Ferienhaus 'klein, aber fein' in ruhiger Lager mit großem Grundstück.
Homepage: dunenhof-kelting.de
Aufgabenstellung
Format DIN LANG / 4 Seiten: Es sollen keine Saisonzeiten und auch keine Preise genannt werden. Es soll nur genannt werden, dass das Haus ab 50 EUR / Tag gemietet werden kann. Bitte nicht die vollständige Adresse des Objektes angeben, lediglich „Sylt-Archsum“. Kontakdtaen bitte auf der Rückseite nennen (siehe Homepage). Kontaktaufnahme bevorzugt per Mail / Anfrageformular v. Homepage. Gerne meine Bilder nutzen, bin aber auch offen für 2-3 Bilder aus dem Stock. Kleine Texte formulieren und gerne mehrere Bilder des Hauses zeigen.

```html
<!DOCTYPE html>
<html lang="de">
<head>
<meta charset="utf-8">
<title>Dünenhof Kelting – Flyer</title>
<link href="https://fonts.googleapis.com/css2?family=Libre+Baskerville&family=Nunito+Sans:wght@400;600&family=Source+Sans+3:wght@600&family=Alex+Brush&display=swap" rel="stylesheet">
<style>
:root{
  --page:#c4c4c4;
  --band:#4b7ba6;
  --ink-blue:#2e6c9c;
  --ink:#1e1e1e;
  --paper:#ffffff;
}
*{box-sizing:border-box;margin:0;padding:0}
html,body{width:667px;height:1200px;overflow:hidden;background:var(--page)}
body{position:relative;font-family:"Nunito Sans",sans-serif;color:var(--ink)}
.abs{position:absolute}
.panel{position:absolute;background:var(--paper);overflow:hidden;box-shadow:0 0 2px rgba(0,0,0,.12)}
.photo{position:absolute;overflow:hidden}
.band{position:absolute;background:var(--band);color:#fff;text-align:center}
.brand{font-family:"Libre Baskerville",serif;font-weight:400;white-space:nowrap}
.script{font-family:"Alex Brush",cursive;white-space:nowrap}
.mark{position:absolute;border-radius:50%}
.center{position:absolute;left:0;right:0;text-align:center}

/* photo areas: soft tonal fills in each picture's main colours */
.ph-house-field{background:linear-gradient(180deg,#b9dcec 0%,#a4c98e 52%,#6f9a45 100%)}
.ph-house-near{background:linear-gradient(180deg,#7dbfe0 0%,#a86a52 48%,#6aa33e 100%)}
.ph-beach-light{background:linear-gradient(180deg,#8fb2cd 0%,#b7c2bf 38%,#d3b867 64%,#d8c8a6 100%)}
.ph-sunset{background:linear-gradient(180deg,#f0b36a 0%,#a5673a 45%,#4d4630 100%)}
.ph-boardwalk{background:linear-gradient(180deg,#7e9ccb 0%,#a4ae86 50%,#c9ad86 100%)}
.ph-dunes-bench{background:linear-gradient(180deg,#96c2e6 0%,#e3e2da 55%,#aeb17d 100%)}
.ph-cliff{background:linear-gradient(180deg,#b6cfe2 0%,#a89584 45%,#7e4128 100%)}
.ph-terrace{background:linear-gradient(180deg,#9c5a47 0%,#c9b4aa 50%,#d8d8d4 72%,#7ea64c 100%)}
.ph-terrace2{background:linear-gradient(180deg,#a46049 0%,#c9aea4 45%,#d9d8d4 100%)}
.ph-bubbly{background:linear-gradient(180deg,#95c0e2 0%,#7ea65a 45%,#c87a9c 70%,#4b6a3e 100%)}
.ph-kitchen{background:linear-gradient(180deg,#e6d9bd 0%,#f2efe8 55%,#e6dcc4 100%)}
.ph-dining{background:linear-gradient(180deg,#f0efeb 0%,#ddd3c2 50%,#a9773f 100%)}
.ph-living{background:linear-gradient(180deg,#dde1e8 0%,#8a97c2 55%,#a57a48 100%)}
.ph-bedroom2{background:linear-gradient(180deg,#efedeb 0%,#e2d3bd 50%,#bf915a 100%)}
.ph-bath{background:linear-gradient(180deg,#f1efea 0%,#d6d1c6 50%,#55575d 100%)}
.ph-bedroom{background:linear-gradient(180deg,#f0eeeb 0%,#8f93b6 50%,#c69d68 100%)}

/* text blocks */
.cta-intro{font-family:"Source Sans 3",sans-serif;font-weight:600;color:var(--ink-blue);font-size:10px;line-height:13.5px}
.contact-line{font-family:"Source Sans 3",sans-serif;font-weight:600;font-size:10.5px;color:var(--ink)}
.rule{position:absolute;height:0;border-top:0.6px solid var(--ink-blue)}
.phones{font-size:7.6px;letter-spacing:0.05px}
.features{font-size:8px;line-height:13.5px}
.about p{font-size:8px;line-height:10.7px;text-align:justify;text-align-last:left}
</style>
</head>
<body>

<!-- Spread 1: back and front -->
<section class="panel" style="left:69px;top:44px;width:535px;height:535px">
  <!-- back page -->
  <div class="photo ph-house-field" style="left:0;top:0;width:268px;height:123px" role="img" aria-label="Foto: Ferienhaus mit Spitzdach hinter Feld und Hecken"></div>
  <div class="band" style="left:0;top:122px;width:268px;height:66px">
    <div class="center brand" style="top:16px;font-size:17.5px">Dünenhof Kelting</div>
    <div class="center" style="top:41px;font-size:9.5px;font-weight:400">Sylt-Archsum</div>
  </div>
  <div class="mark" style="left:119px;top:105px;width:30px;height:30px;background:#fff"></div>

  <div class="center cta-intro" style="top:200px;width:268px">Bevorzugt Buchungsanfragen per E-Mail<br>oder Online-Kontaktformular:</div>
  <div class="rule" style="left:42px;top:234px;width:182px"></div>
  <div class="center contact-line" style="top:239px;width:268px">strandkatenmoorum@web.de</div>
  <div class="center contact-line" style="top:256px;width:268px">dunenhof-kelting.de</div>
  <div class="rule" style="left:42px;top:274px;width:182px"></div>
  <div class="center phones" style="top:288px;width:268px">T: 030 555 104 27&nbsp; | &nbsp;M: 0170 55 512 64&nbsp; | &nbsp;F: 030 555 104 28</div>

  <div class="photo ph-sunset" style="left:0;top:313px;width:132px;height:110px" role="img" aria-label="Foto: Sonnenuntergang über Landstraße mit Heckenrosen"></div>
  <div class="photo ph-boardwalk" style="left:134px;top:313px;width:134px;height:110px" role="img" aria-label="Foto: Holzsteg durch die Dünen zum Meer"></div>
  <div class="photo ph-dunes-bench" style="left:0;top:425px;width:132px;height:110px" role="img" aria-label="Foto: Dünenweg mit Bank am Strand"></div>
  <div class="photo ph-cliff" style="left:134px;top:425px;width:134px;height:110px" role="img" aria-label="Foto: Rotes Kliff mit Strandkörben am Meer"></div>
  <div class="photo ph-house-near" style="left:78px;top:368px;width:110px;height:110px;border-radius:50%;border:2px solid #fff" role="img" aria-label="Foto: Ferienhaus mit Rundfenstern, rund ausgeschnitten"></div>

  <!-- front page -->
  <div class="photo ph-house-near" style="left:268px;top:0;width:267px;height:274px" role="img" aria-label="Foto: Backsteinhaus mit Spitzdach und weißer Tür im Garten"></div>
  <div class="band" style="left:268px;top:274px;width:267px;height:46px">
    <div class="center brand" style="top:9px;font-size:25px">Dünenhof Kelting</div>
  </div>
  <div class="mark" style="left:373px;top:216px;width:66px;height:66px;background:#fff"></div>
  <div class="photo ph-beach-light" style="left:268px;top:321px;width:267px;height:214px" role="img" aria-label="Foto: Dünen mit Strandhafer und rot-weißem Leuchtturm am Meer"></div>
  <div class="abs script" style="left:268px;width:240px;top:337px;text-align:center;color:#fff;font-size:27px;line-height:27px">Ankommen und<br>wohlfühlen</div>
</section>

<!-- Spread 2: inside -->
<section class="panel" style="left:69px;top:622px;width:535px;height:535px">
  <!-- left inside page -->
  <div class="photo ph-terrace" style="left:0;top:0;width:267px;height:125px" role="img" aria-label="Foto: Südterrasse mit Gartenmöbeln und Strandkorb"></div>
  <div class="photo ph-terrace2" style="left:0;top:128px;width:148px;height:97px" role="img" aria-label="Foto: Gedeckter Terrassentisch vor dem Haus"></div>
  <div class="photo ph-bubbly" style="left:151px;top:128px;width:116px;height:97px" role="img" aria-label="Foto: Sekt und Blumen auf dem Gartentisch"></div>
  <div class="photo ph-kitchen" style="left:0;top:228px;width:128px;height:101px" role="img" aria-label="Foto: Helle Einbauküche"></div>
  <div class="photo ph-dining" style="left:131px;top:228px;width:136px;height:101px" role="img" aria-label="Foto: Essbereich mit Holztisch"></div>

  <div class="abs script" style="left:0;width:267px;top:339px;text-align:center;color:var(--ink-blue);font-size:19px">Ankommen und wohlfühlen</div>
  <ul class="abs features" style="left:0;width:267px;top:368px;list-style:none;text-align:center">
    <li>Lichtdurchflutetes Wohnzimmer mit ausziehbarer Couch</li>
    <li>Moderne offene Einbauküche</li>
    <li>Schlafzimmer mit Doppelbett</li>
    <li>Zweites Schlafzimmer/Kinderzimmer</li>
    <li>Badezimmer im Ober- und Erdgeschoss</li>
    <li>Waschtrockner</li>
    <li>Fußbodenheizung</li>
    <li>Südterrasse mit Strandkorb</li>
    <li>PKW-Stellplatz direkt am Haus</li>
    <li>Kostenfreies WLAN</li>
    <li>Kontaktlose Anreise mit persönlichem Pin-Code</li>
  </ul>

  <!-- right inside page -->
  <div class="mark" style="left:383px;top:21px;width:42px;height:42px;background:var(--ink-blue)"></div>
  <div class="abs brand" style="left:267px;width:268px;top:63px;text-align:center;color:var(--ink-blue);font-size:18.5px">Dünenhof Kelting</div>
  <div class="abs about" style="left:298px;width:208px;top:105px">
    <p>Kleines aber feines Ferienhaus im traditionellen Ort Archsum auf Sylt in ruhiger Lage mit großem Garten.</p>
    <p style="margin-top:19px">Das freistehende, massiv gebaute Ferienhaus bietet Ruhe- und Erholungssuchenden mit 86 m² Wohnfläche, der schönen Süd-Terrasse und dem großen Grundstück (1200 m²) die besten Voraussetzungen zum Entspannen, Sonne tanken und um sich einfach nur wohlzufühlen.</p>
    <p style="margin-top:10px">Ideal für 2-6 Personen<br>Verfügbar bereits ab € 50,- Tagesmiete</p>
  </div>

  <div class="photo ph-living" style="left:267px;top:269px;width:154px;height:111px" role="img" aria-label="Foto: Wohnzimmer mit blauer Ecksofa-Couch"></div>
  <div class="photo ph-bedroom2" style="left:424px;top:269px;width:111px;height:111px" role="img" aria-label="Foto: Kinderzimmer unter der Dachschräge"></div>
  <div class="photo ph-bath" style="left:267px;top:383px;width:129px;height:105px" role="img" aria-label="Foto: Modernes Badezimmer mit Waschtisch"></div>
  <div class="photo ph-bedroom" style="left:399px;top:383px;width:136px;height:105px" role="img" aria-label="Foto: Schlafzimmer mit Doppelbett"></div>

  <div class="band" style="left:267px;top:492px;width:268px;height:43px">
    <div class="center" style="top:6px;font-size:8px">Alle Details und Buchungsmöglichkeit auf</div>
    <div class="center brand" style="top:18px;font-size:11.5px">dunenhof-kelting.de</div>
  </div>
</section>

</body>
</html>
```